Crestline Marketing Business Card

Business card using new logo for marketing consulting company based in Silicon Valley. Limited information on card now (name, phone number, email, website), but room to add mailing address later.

```html
<!DOCTYPE html>
<html lang="en">
<head>
<meta charset="utf-8">
<title>Crestline Marketing – Business Card</title>
<link rel="stylesheet" href="https://fonts.googleapis.com/css2?family=Arimo:wght@400;700&display=swap">
<style>
  :root {
    --sheet-bg: #ffffff;
    --sheet-frame: #4a5080;
    --label-ink: #1a1a1a;
    --sky: #00a8df;
    --sky-light: #6fd0f0;
    --navy: #353c6b;
    --paper: #ffffff;
    --paper-shade: #e4e6ea;
    --ink-white: #ffffff;
    --brand-blue: #1fa3da;
  }
  * { box-sizing: border-box; margin: 0; padding: 0; }
  html, body { width: 900px; height: 1200px; overflow: hidden; background: var(--sheet-bg); }
  body { position: relative; font-family: "Arimo", Arial, sans-serif; }

  .sheet-frame {
    position: absolute; left: 1px; top: 1px; width: 898px; height: 1198px;
    border: 2px solid var(--sheet-frame);
  }
  .side-label {
    position: absolute; left: 52px; font-size: 29px; color: var(--label-ink); font-weight: 400;
  }
  .side-label--front { top: 24px; }
  .side-label--rear { top: 616px; }

  .card {
    position: absolute; left: 52px; width: 798px; height: 516px; overflow: hidden;
  }
  .card--front { top: 72px; background: var(--sky); }
  .card--rear { top: 664px; background: var(--navy); }

  .card-shape { position: absolute; inset: 0; width: 100%; height: 100%; }

  .bubble-field {
    position: absolute; left: 480px; top: 0; width: 318px; height: 290px;
    background: radial-gradient(ellipse at 60% 45%, rgba(255,255,255,0.16), rgba(255,255,255,0) 70%);
  }

  .brand-mark {
    position: absolute; display: flex; flex-direction: column; align-items: center;
    color: var(--brand-blue); font-weight: 400; text-align: center;
  }
  .brand-mark__dot { border-radius: 50%; background: var(--brand-blue); }
  .brand-mark--front { left: 20px; top: 150px; width: 240px; gap: 22px; }
  .brand-mark--front .brand-mark__dot { width: 56px; height: 56px; }
  .brand-mark--front .brand-mark__name { font-size: 22px; letter-spacing: 0.5px; line-height: 1.25; }
  .brand-mark--rear { left: 199px; top: 120px; width: 400px; gap: 48px; }
  .brand-mark--rear .brand-mark__dot { width: 110px; height: 110px; }
  .brand-mark--rear .brand-mark__name { font-size: 38px; letter-spacing: 1px; line-height: 1.25; }

  .holder {
    position: absolute; right: 40px; top: 90px; text-align: right; color: var(--ink-white);
  }
  .holder__name { font-size: 28px; font-weight: 700; line-height: 34px; }
  .holder__title { font-size: 23px; font-weight: 400; line-height: 32px; }

  .contact-list {
    position: absolute; right: 38px; top: 295px; list-style: none; color: var(--ink-white);
    font-size: 19px; line-height: 1;
  }
  .contact-list__item {
    display: flex; justify-content: flex-end; align-items: center; gap: 12px; height: 36px;
  }
  .contact-list__item--address { align-items: flex-start; height: auto; padding-top: 4px; }
  .contact-list__text { text-align: right; line-height: 29px; }
  .contact-list__item--address .contact-list__text { line-height: 28px; margin-top: -4px; }
  .contact-icon { width: 22px; height: 22px; flex: none; }
</style>
</head>
<body>
  <div class="sheet-frame"></div>

  <div class="side-label side-label--front">card_infront</div>
  <section class="card card--front" aria-label="Card front">
    <svg class="card-shape" viewBox="0 0 798 516" aria-hidden="true">
      <defs>
        <radialGradient id="paperGlow" cx="35%" cy="45%" r="70%">
          <stop offset="0" stop-color="var(--paper)"/>
          <stop offset="1" stop-color="var(--paper-shade)"/>
        </radialGradient>
      </defs>
      <path d="M0,0 L308,0 C360,140 350,370 164,516 L0,516 Z" fill="var(--sky-light)"/>
      <path d="M0,0 L296,0 C346,140 336,370 148,516 L0,516 Z" fill="var(--navy)"/>
      <path d="M0,0 L276,0 C324,140 314,370 112,516 L0,516 Z" fill="url(#paperGlow)"/>
    </svg>
    <div class="bubble-field" role="img" aria-label="Soft pattern of translucent light-blue circles"></div>

    <div class="brand-mark brand-mark--front">
      <span class="brand-mark__dot"></span>
      <span class="brand-mark__name">CRESTLINE MARKETING</span>
    </div>

    <div class="holder">
      <p class="holder__name">Name N. Name</p>
      <p class="holder__title">DESIGNATION</p>
    </div>

    <ul class="contact-list">
      <li class="contact-list__item">
        <span class="contact-list__text">+254 700 123 456</span>
        <svg class="contact-icon" viewBox="0 0 22 22" aria-hidden="true"><rect x="1" y="1" width="20" height="20" rx="4" fill="none" stroke="#fff" stroke-width="1.6"/><path d="M5 9 Q11 4 17 9 L15 11 L13 9 L9 9 L7 11 Z M7 12 H15 V16 H7 Z" fill="#fff"/></svg>
      </li>
      <li class="contact-list__item">
        <span class="contact-list__text">+254 700 123 456</span>
        <svg class="contact-icon" viewBox="0 0 22 22" aria-hidden="true"><rect x="1" y="1" width="20" height="20" rx="4" fill="none" stroke="#fff" stroke-width="1.6"/><rect x="8" y="4" width="6" height="14" rx="1.2" fill="#fff"/><rect x="9.2" y="6" width="3.6" height="5" fill="var(--sky)"/></svg>
      </li>
      <li class="contact-list__item">
        <span class="contact-list__text">sales@crestline-mktg.net</span>
        <svg class="contact-icon" viewBox="0 0 22 22" aria-hidden="true"><rect x="1" y="1" width="20" height="20" rx="4" fill="none" stroke="#fff" stroke-width="1.6"/><text x="11" y="16" text-anchor="middle" font-family="Arimo, Arial, sans-serif" font-size="14" font-weight="700" fill="#fff">@</text></svg>
      </li>
      <li class="contact-list__item">
        <span class="contact-list__text">www.crestline-mktg.net</span>
        <svg class="contact-icon" viewBox="0 0 22 22" aria-hidden="true"><rect x="1" y="1" width="20" height="20" rx="4" fill="none" stroke="#fff" stroke-width="1.6"/><circle cx="11" cy="11" r="6" fill="none" stroke="#fff" stroke-width="1.4"/><ellipse cx="11" cy="11" rx="2.6" ry="6" fill="none" stroke="#fff" stroke-width="1.1"/><path d="M5 11 H17" stroke="#fff" stroke-width="1.1"/></svg>
      </li>
      <li class="contact-list__item contact-list__item--address">
        <span class="contact-list__text">P.O. BOX 000 - 000&nbsp; Silicon<br>Av&nbsp; Silicon Valley</span>
        <svg class="contact-icon" viewBox="0 0 22 22" aria-hidden="true"><rect x="1" y="1" width="20" height="20" rx="4" fill="none" stroke="#fff" stroke-width="1.6"/><rect x="5" y="6.5" width="12" height="9" fill="none" stroke="#fff" stroke-width="1.4"/><path d="M5 6.5 L11 11.5 L17 6.5" fill="none" stroke="#fff" stroke-width="1.4"/></svg>
      </li>
    </ul>
  </section>

  <div class="side-label side-label--rear">card_rear</div>
  <section class="card card--rear" aria-label="Card back">
    <svg class="card-shape" viewBox="0 0 798 516" aria-hidden="true">
      <defs>
        <radialGradient id="rearGlow" cx="50%" cy="50%" r="55%">
          <stop offset="0" stop-color="var(--paper)"/>
          <stop offset="1" stop-color="var(--paper-shade)"/>
        </radialGradient>
      </defs>
      <circle cx="400" cy="256" r="316" fill="var(--paper)"/>
      <circle cx="400" cy="256" r="304" fill="var(--sky)"/>
      <circle cx="400" cy="256" r="293" fill="var(--paper)"/>
      <circle cx="400" cy="256" r="285" fill="url(#rearGlow)"/>
    </svg>
    <div class="brand-mark brand-mark--rear">
      <span class="brand-mark__dot"></span>
      <span class="brand-mark__name">CRESTLINE MARKETING</span>
    </div>
  </section>
</body>
</html>
```